Lumora MediSpa - Mailchimp Email

I have a list of prospects that I want to email. I'm using Mailchimp. I would like my template to explain that we are now open and ready for business. We are offering 20% off on all services and special procedure combination deals. I want the design to be a template that I can use the same look and feel for future emails - for information giving, beauty tips. monthly promos, etc.

I don't know much about email campaigns, but I'd like to keep it simple, let the people know we're open for business and try to get them to either respond to the email or call for a free consult.
Updates

Thank you all for your hard work on my project.

Target Market(s)

The list criteria is female, income greater than $50,000, between the age of 30 and 65. The area is affluent - Potomac, Bethesda and Chevy Chase Maryland

Industry/Entity Type

Health And Wellness

Font styles to use
Other font styles liked:
• I'd like to keep the font simple like our logo font - again if possible.

Colors

Designer to choose colors to be used in the design.

Requirements
Must have
• my logo, nice pictures related to the medispa business, location "1 block from Harrowgate Crossing Mall', link to our website
Nice to have
• place to input their info to sign up for future emails - i see this on websites. I don't know if they do this for emails. Mailchimp seems to use them.
• Keep the look and feel of our website if that makes sense - www.lumoramedispa.example.
Should not have
• don't be too busy or too long. Keep it simple if possible.

```html
<!DOCTYPE html>
<html lang="en">
<head>
<meta charset="utf-8">
<title>Lumora MediSpa – Now Open</title>
<link href="https://fonts.googleapis.com/css2?family=Lato:wght@400;700&family=Roboto+Condensed:wght@500;700&display=swap" rel="stylesheet">
<style>
  :root{
    --green:#6b9a2f;
    --green-dark:#5a8426;
    --ink:#333333;
    --muted:#555555;
    --panel:#efefef;
    --band:#2e2e2e;
    --white:#ffffff;
  }
  *{box-sizing:border-box;margin:0;padding:0}
  html,body{width:681px;height:1200px;overflow:hidden;background:var(--white)}
  body{font-family:"Lato",Arial,sans-serif;color:var(--ink);position:relative}
  .email{width:681px;height:1200px;position:relative}

  .header{height:92px;display:flex;justify-content:space-between;align-items:center;padding:0 24px 0 22px}
  .brand{display:flex;align-items:center;gap:10px}
  .brand-dot{width:30px;height:30px;border-radius:50%;background:var(--green)}
  .brand-name{font-family:"Lato",Arial,sans-serif;font-weight:700;font-size:27px;color:var(--ink);letter-spacing:.5px}
  .contact{font-size:12.5px;color:var(--ink);line-height:1.5}
  .contact-row{display:flex;gap:10px;align-items:flex-start}
  .contact-row svg{flex:none;margin-top:2px}
  .contact-row + .contact-row{margin-top:6px}

  .hero{height:178px;background:linear-gradient(100deg,#d9d9d9 0%,#bdbdbd 40%,#e2e2e2 75%,#cfcfcf 100%)}

  .intro{height:200px;position:relative}
  .intro-copy{position:absolute;left:38px;top:36px;width:290px;text-align:center;font-size:15px;line-height:1.55;color:var(--muted)}
  .offer{position:absolute;left:360px;top:38px;width:290px;text-align:center;color:var(--green-dark)}
  .offer-lead{font-family:"Roboto Condensed",Arial,sans-serif;font-weight:700;font-size:24px}
  .offer-big{font-family:"Roboto Condensed",Arial,sans-serif;font-weight:500;font-size:62px;line-height:1}
  .offer-note{font-family:"Roboto Condensed",Arial,sans-serif;font-weight:700;font-size:14px;color:var(--ink);line-height:1.3;margin-top:4px}
  .btn{display:block;position:absolute;left:50%;transform:translateX(-50%);height:34px;border:2px solid var(--green);background:var(--white);font-family:"Roboto Condensed",Arial,sans-serif;font-weight:700;font-size:13px;letter-spacing:.8px;color:var(--ink);text-align:center;line-height:30px;text-decoration:none}
  .btn-explore{top:144px;width:152px}

  .services{position:absolute;left:0;top:470px;width:681px;height:530px;background:var(--panel)}
  .services-title{position:absolute;top:30px;width:100%;text-align:center;font-family:"Roboto Condensed",Arial,sans-serif;font-weight:700;font-size:34px;color:var(--green)}
  .service-photo{position:absolute;width:306px;height:156px}
  .photo-facial{left:22px;top:68px;background:linear-gradient(120deg,#6f5a4d 0%,#c9b3a4 45%,#e8d9cc 100%)}
  .photo-laser{left:353px;top:226px;background:linear-gradient(110deg,#b59886 0%,#dcc4b4 50%,#a8c4bf 100%)}
  .service-text{position:absolute;width:290px;text-align:center}
  .text-facial{left:360px;top:100px}
  .text-laser{left:20px;top:250px;text-align:left;width:300px}
  .service-name{font-family:"Roboto Condensed",Arial,sans-serif;font-weight:700;font-size:20px;color:var(--green);margin-bottom:8px}
  .service-desc{font-size:14px;line-height:1.5;color:var(--muted)}
  .btn-services{top:466px;width:164px}

  .cta-band{position:absolute;left:0;top:1000px;width:681px;height:86px;background:var(--band);color:var(--white);display:flex;align-items:center;justify-content:space-between;padding:0 80px 0 100px}
  .cta-call{text-align:center}
  .cta-label{font-size:14px;font-weight:700}
  .cta-phone{font-size:22px;font-weight:700;letter-spacing:.5px}
  .cta-web{display:flex;align-items:center;gap:12px;font-size:14px}

  .footer{position:absolute;left:0;top:1086px;width:681px;height:114px;text-align:center}
  .social{display:flex;justify-content:center;gap:12px;margin-top:30px}
  .social span{width:24px;height:24px;border-radius:50%;background:var(--green);display:block}
  .copyright{font-size:12px;color:var(--muted);margin-top:20px}
</style>
</head>
<body>
<div class="email">
  <header class="header">
    <div class="brand">
      <span class="brand-dot"></span>
      <span class="brand-name">Lumora MediSpa</span>
    </div>
    <div class="contact">
      <div class="contact-row">
        <svg width="13" height="13" viewBox="0 0 24 24"><path fill="#6b9a2f" d="M6.6 10.8a15.1 15.1 0 0 0 6.6 6.6l2.2-2.2c.3-.3.7-.4 1-.2 1.1.4 2.3.6 3.6.6.6 0 1 .4 1 1V20c0 .6-.4 1-1 1A17 17 0 0 1 3 4c0-.6.4-1 1-1h3.5c.6 0 1 .4 1 1 0 1.3.2 2.5.6 3.6.1.3 0 .7-.2 1z"/></svg>
        <span>301.555.0147</span>
      </div>
      <div class="contact-row">
        <svg width="13" height="15" viewBox="0 0 24 24"><path fill="#6b9a2f" d="M12 2a7 7 0 0 0-7 7c0 5.2 7 13 7 13s7-7.8 7-13a7 7 0 0 0-7-7zm0 9.5A2.5 2.5 0 1 1 12 6.5a2.5 2.5 0 0 1 0 5z"/></svg>
        <span>2190 Linden Park Way | Suite B-204 |<br>Bethesda, MD</span>
      </div>
    </div>
  </header>

  <div class="hero" role="img" aria-label="Photo of a relaxing facial mask treatment at the spa"></div>

  <section class="intro">
    <p class="intro-copy">Our goals are natural beauty and patient satisfaction. We strive to make sure you are happy with your look. We are commited to enhance your natural beauty.</p>
    <div class="offer">
      <div class="offer-lead">We are offering</div>
      <div class="offer-big">20% off</div>
      <div class="offer-note">on all services and special<br>procedure combination deals</div>
    </div>
    <a class="btn btn-explore" href="#">EXPLORE</a>
  </section>

  <section class="services">
    <h2 class="services-title">SERVICES</h2>
    <div class="service-photo photo-facial" role="img" aria-label="Photo of a client receiving a gentle facial massage"></div>
    <div class="service-text text-facial">
      <h3 class="service-name">FACIAL AESTHETICS</h3>
      <p class="service-desc">"Neurotox" or use of Neuromodulators utilizing Botulinum Toxin A, is the most popular noninvasive cosmetic procedure available.</p>
    </div>
    <div class="service-text text-laser">
      <h3 class="service-name">LASER SKIN TREATMENTS</h3>
      <p class="service-desc">Laser skin rejuvenation is designed to improve the skin's appearance by treating wrinkles, sun damage, sagging skin, brown spots and more.</p>
    </div>
    <div class="service-photo photo-laser" role="img" aria-label="Photo of a woman with smooth, glowing skin"></div>
    <a class="btn btn-services" href="#">VIEW ALL SERVICES</a>
  </section>

  <section class="cta-band">
    <div class="cta-call">
      <div class="cta-label">Call for a free consultation</div>
      <div class="cta-phone">301.555.0147</div>
    </div>
    <div class="cta-web">
      <svg width="22" height="22" viewBox="0 0 24 24" fill="none" stroke="#ffffff" stroke-width="1.6"><circle cx="12" cy="12" r="9.5"/><ellipse cx="12" cy="12" rx="4" ry="9.5"/><path d="M2.5 12h19M4 7h16M4 17h16"/></svg>
      <span>https://www.lumoramedispa.example/</span>
    </div>
  </section>

  <footer class="footer">
    <div class="social"><span></span><span></span><span></span></div>
    <p class="copyright">Copyright © 2019 Lumora Medi Spa. All Rights Reserved.</p>
  </footer>
</div>
</body>
</html>
```